Brightway Haul & Repair Services, are a company that offers a 'one stop shop' pre-move clean up a

I have already selected a logo which I would like on the front of the business cards along with phone numbers, web address and email which are:
0419574302
www.brightwayhaul.com.au
brightwayhaulrepair@mailbox.example

On the back of the card I would like to list some of the types of service we offer (clean - move - repairs/maintenance) which are:
CLEAN - windows, gutters, solar panels, driveways/paths, carpets.
MOVE - Small/medium size house/office moves, large item pick-up & delivery, yard clean-up and removal.
General maintenance and repairs.

I would like the blue logo on a gray background.

Thanks

```html
<!DOCTYPE html>
<html lang="en">
<head>
<meta charset="utf-8">
<title>Brightway Haul &amp; Repair Services – Business Card</title>
<link rel="stylesheet" href="https://fonts.googleapis.com/css2?family=Arimo:wght@400;700&display=swap">
<style>
  :root {
    --page-bg: #ffffff;
    --card-grey-light: #d6d7d9;
    --card-grey-mid: #b9babd;
    --card-grey-dark: #8f9094;
    --accent-blue: #1f6db5;
    --sky-pale: #a9cde8;
    --sky-bright: #74b9e6;
    --text-blue: #2a6fb7;
  }
  html, body {
    margin: 0;
    padding: 0;
    width: 1200px;
    height: 927px;
    overflow: hidden;
    background: var(--page-bg);
  }
  .canvas {
    position: relative;
    width: 1200px;
    height: 927px;
    font-family: "Arimo", Arial, sans-serif;
  }
  .card-art {
    position: absolute;
    left: 0;
    top: 0;
  }
  .brand-name {
    position: absolute;
    left: 76px;
    top: 318px;
    margin: 0;
    font-size: 50px;
    font-weight: 700;
    line-height: 1.08;
    color: var(--accent-blue);
    letter-spacing: 0.5px;
  }
  .contact {
    position: absolute;
    left: 75px;
    top: 588px;
    margin: 0;
    font-size: 33px;
    font-weight: 400;
    line-height: 41px;
    color: var(--text-blue);
  }
  .contact-line { display: block; }
  .contact-line.indented { padding-left: 161px; }
</style>
</head>
<body>
<main class="canvas">
  <svg class="card-art" width="1200" height="927" viewBox="0 0 1200 927" aria-hidden="true">
    <defs>
      <radialGradient id="cardGrey" cx="345" cy="520" r="720" gradientUnits="userSpaceOnUse">
        <stop offset="0" stop-color="var(--card-grey-light)"/>
        <stop offset="0.6" stop-color="var(--card-grey-mid)"/>
        <stop offset="1" stop-color="var(--card-grey-dark)"/>
      </radialGradient>
      <clipPath id="cardShape">
        <rect x="27" y="195" width="981" height="578" rx="46"/>
      </clipPath>
    </defs>
    <g clip-path="url(#cardShape)">
      <rect class="card-face" x="27" y="195" width="981" height="578" fill="url(#cardGrey)"/>
      <circle cx="735" cy="300" r="395" fill="var(--sky-pale)" opacity="0.55"/>
      <circle cx="750" cy="690" r="385" fill="var(--sky-pale)" opacity="0.35"/>
      <circle cx="1150" cy="340" r="420" fill="var(--sky-bright)" opacity="0.75"/>
    </g>
  </svg>

  <h1 class="brand-name">Brightway Haul<br>&amp; Repair Services</h1>

  <p class="contact">
    <span class="contact-line">Contact: 0419574302</span>
    <span class="contact-line indented">www.brightwayhaul.com.au</span>
    <span class="contact-line indented">brightwayhaulrepair@mailbox.example</span>
  </p>
</main>
</body>
</html>
```